Naturopath Practitioner Card Design

I am a naturopath needing a design for a business card mainly to show that I am a naturopath and have some contact details to give to prospective clients. I am open minded about the design and what is on the second side of the card whether it just be some artwork or space for details, appointment times etc. Naturopathy is the practice of natural medicine that uses a holistic approach and incorporates herbal and nutritional medicine.

Contact Information for Business Card

Tom Waverly NaturopathBHSc (Naturopathy) Member NHPG 0491 582 736 tom.waverly@mailbox-example.net www.tomwaverlynaturopathy.example.au

Requirements
Nice to have
• Would prefer some kind of original pattern/art work/logo rather than an image, not fussed if its very simple/basic
• I am open to any colour but think I would prefer a more earthy sandy clay etc type style than the greens that are commonly associated with naturopathy.
Should not have
• Don't really want to have generic stock images on it

```html
<!DOCTYPE html>
<html lang="en">
<head>
<meta charset="utf-8">
<title>Naturopath Business Card</title>
<link rel="stylesheet" href="https://fonts.googleapis.com/css2?family=Open+Sans:wght@400;600;700&display=swap">
<style>
  :root {
    --page-bg: #2b2b2b;
    --card-white: #ffffff;
    --card-dark: #333333;
    --leaf-green: #7dc242;
    --ink: #1a1a1a;
    --rule: #444444;
    --text-light: #f2f2f2;
  }
  * { box-sizing: border-box; margin: 0; padding: 0; }
  html, body {
    width: 1200px; height: 900px; overflow: hidden;
    background: var(--page-bg);
    font-family: "Open Sans", Arial, sans-serif;
  }
  .stage {
    width: 1200px; height: 900px;
    display: flex; flex-direction: column; align-items: center; justify-content: center;
    gap: 56px;
  }
  .card {
    width: 560px; height: 320px; position: relative; overflow: hidden;
    box-shadow: 0 10px 28px rgba(0,0,0,0.45);
  }
  .practice-name {
    font-family: "Open Sans", Arial, sans-serif;
    font-weight: 600;
    color: var(--leaf-green);
    line-height: 1;
    display: inline-flex; align-items: center; gap: 10px;
  }
  .practice-mark {
    width: 12px; height: 12px; border-radius: 50%;
    background: var(--leaf-green); flex: none;
  }

  /* Appointment side */
  .card--appointment { background: var(--card-white); }
  .appointment-head { text-align: center; padding-top: 36px; }
  .appointment-head .practice-name { font-size: 40px; }
  .membership { font-size: 22px; color: var(--ink); margin-top: 10px; }
  .appointment-label {
    font-size: 12px; letter-spacing: 0.08em; color: var(--leaf-green); margin-top: 8px;
  }
  .appointment-fields { position: absolute; left: 44px; right: 44px; bottom: 34px; }
  .field { display: flex; align-items: flex-end; gap: 6px; margin-top: 24px; }
  .field-label { font-size: 15px; color: var(--ink); }
  .field-line { flex: 1; border-bottom: 1px solid var(--rule); height: 1px; margin-bottom: 4px; }

  /* Contact side */
  .card--contact { background: var(--card-dark); }
  .herb-art {
    position: absolute; left: 60px; top: 30px; width: 420px; height: 270px;
    background: radial-gradient(ellipse at 50% 45%, #5e5e5e 0%, #3e4a36 35%, #26331f 60%, rgba(51,51,51,0) 78%);
  }
  .card--contact .practice-name {
    position: absolute; left: 170px; top: 96px; font-size: 40px;
  }
  .contact-block { position: absolute; left: 290px; top: 158px; width: 250px; }
  .person-name {
    font-weight: 700; font-size: 19px; color: var(--leaf-green); letter-spacing: 0.02em;
  }
  .person-role { font-size: 12px; color: var(--text-light); letter-spacing: 0.03em; margin-top: 2px; }
  .contact-lines { margin-top: 10px; font-size: 12px; color: var(--text-light); line-height: 1.7; }
  .contact-lines b { color: var(--leaf-green); font-weight: 700; margin-right: 4px; }
</style>
</head>
<body>
<main class="stage">
  <section class="card card--appointment">
    <header class="appointment-head">
      <h1 class="practice-name"><span class="practice-mark"></span>Naturopathy</h1>
      <p class="membership">Member NHPG</p>
      <p class="appointment-label">APPOINTMENT</p>
    </header>
    <div class="appointment-fields">
      <div class="field"><span class="field-label">Name:</span><span class="field-line"></span></div>
      <div class="field"><span class="field-label">Time:</span><span class="field-line"></span></div>
      <div class="field"><span class="field-label">Date:</span><span class="field-line"></span></div>
    </div>
  </section>

  <section class="card card--contact">
    <div class="herb-art" role="img" aria-label="White mortar and pestle among fresh green herbs and cinnamon sticks"></div>
    <h2 class="practice-name"><span class="practice-mark"></span>Naturopathy</h2>
    <div class="contact-block">
      <p class="person-name">TOM WAVERLY</p>
      <p class="person-role">NATUROPATH (BHSC)</p>
      <p class="contact-lines"><b>P:</b>0491 582 736<br><b>E:</b>tom.waverly@mailbox-example.net</p>
    </div>
  </section>
</main>
</body>
</html>
```